Modern business card and stationary design for Tech consulting company (startup)
Veromb Technologies Limited
Modern business card and stationary design for Tech consulting company (startup) - Information Technology
Creative Brief
Professional
Malcolm Dewhurst
CEO
Suite 24613 Lower Ground Floor 212-224 Harwell Road London, N7 2QD
mdewhurst@veromb.co.uk
www.veromb.co.uk
Designers, This project is for business card and stationary design. What I’m looking for is design based around the colour scheme of the attached logo. As yet the website is still being designed, but the attached business logo will give you a reference point for the corporate colours. I have attached a couple of links with a general idea of what I’m looking for; http://www.plandoria.com/drafts/display/contest/518230/draft/3047612 http://www.plandoria.com/drafts/display/contest/518230/draft/3048945 All submitted designs will be rated on a regular basis. If you have any further questions relating to this project, please let get in touch. The winning design will be required to provide editable versions of the files (i.e. personal contact details etc.) Good luck

```html
<!DOCTYPE html>
<html lang="en">
<head>
<meta charset="utf-8">
<title>Veromb Technologies Limited – Business Card</title>
<link rel="stylesheet" href="https://fonts.googleapis.com/css2?family=Arimo:wght@400;700&display=swap">
<style>
  :root {
    --canvas-bg: #e4e4e4;
    --card-white: #ffffff;
    --card-dark-top: #4a4a4a;
    --card-dark-bottom: #1f1f1f;
    --brand-red: #d3242a;
    --text-grey: #5a5a5a;
    --logo-grey: #3c3c3c;
    --rule-grey: #8a8a8a;
  }
  * { box-sizing: border-box; margin: 0; padding: 0; }
  html, body {
    width: 1200px;
    height: 838px;
    overflow: hidden;
    background: var(--canvas-bg);
    font-family: "Arimo", Arial, sans-serif;
  }
  .stage {
    position: relative;
    width: 1200px;
    height: 838px;
    display: flex;
    align-items: center;
    justify-content: center;
    gap: 40px;
  }
  .card {
    position: relative;
    width: 540px;
    height: 318px;
    box-shadow: 0 10px 28px rgba(0,0,0,0.18);
  }
  .card-front { background: var(--card-white); }
  .card-back {
    background: linear-gradient(160deg, var(--card-dark-top), var(--card-dark-bottom));
    display: flex;
    align-items: center;
    justify-content: center;
    gap: 14px;
  }

  /* Brand wordmark */
  .brand {
    position: absolute;
    top: 34px;
    left: 96px;
    display: flex;
    align-items: center;
    gap: 12px;
  }
  .brand-square {
    width: 30px;
    height: 30px;
    background: var(--brand-red);
  }
  .brand-name {
    font-weight: 700;
    font-size: 30px;
    letter-spacing: 2px;
    color: var(--logo-grey);
    line-height: 1;
  }
  .brand-name small {
    display: block;
    font-size: 13px;
    letter-spacing: 5px;
    margin-top: 4px;
  }

  /* Person */
  .person {
    position: absolute;
    top: 116px;
    left: 30px;
    width: 230px;
    text-align: right;
  }
  .person-name {
    font-weight: 700;
    font-size: 21px;
    color: var(--brand-red);
  }
  .person-role {
    font-size: 13px;
    color: var(--text-grey);
    margin-top: 2px;
  }
  .address {
    position: absolute;
    top: 178px;
    left: 30px;
    width: 230px;
    text-align: right;
    font-size: 13px;
    line-height: 18px;
    color: var(--text-grey);
  }

  .divider {
    position: absolute;
    top: 146px;
    left: 276px;
    width: 1px;
    height: 134px;
    background: var(--rule-grey);
  }

  /* Contact column */
  .contacts {
    position: absolute;
    top: 176px;
    left: 292px;
    list-style: none;
    font-size: 13px;
    line-height: 18px;
    color: var(--text-grey);
  }
  .contacts li {
    display: flex;
    align-items: center;
    gap: 6px;
  }
  .contacts svg {
    width: 11px;
    height: 11px;
    fill: var(--brand-red);
    flex: none;
  }

  /* Back wordmark */
  .back-square {
    width: 44px;
    height: 44px;
    background: var(--brand-red);
  }
  .back-name {
    font-weight: 700;
    font-size: 40px;
    letter-spacing: 3px;
    color: #ffffff;
  }
</style>
</head>
<body>
<main class="stage">
  <section class="card card-front" aria-label="Business card front">
    <div class="brand">
      <span class="brand-square" aria-hidden="true"></span>
      <div class="brand-name">VEROMB<small>TECHNOLOGIES</small></div>
    </div>

    <div class="person">
      <p class="person-name">Malcolm Dewhurst</p>
      <p class="person-role">CEO</p>
    </div>

    <address class="address" style="font-style: normal;">
      Suite 24613<br>
      Lower Ground Floor<br>
      212-224 Harwell Road<br>
      London, N7 2QD
    </address>

    <span class="divider" aria-hidden="true"></span>

    <ul class="contacts">
      <li>
        <svg viewBox="0 0 24 24" aria-hidden="true"><path d="M6.6 10.8a15.1 15.1 0 0 0 6.6 6.6l2.2-2.2a1 1 0 0 1 1-.25 11.4 11.4 0 0 0 3.6.6 1 1 0 0 1 1 1V20a1 1 0 0 1-1 1A17 17 0 0 1 3 4a1 1 0 0 1 1-1h3.5a1 1 0 0 1 1 1c0 1.25.2 2.45.6 3.6a1 1 0 0 1-.25 1z"/></svg>
        +44 (0)845 3917720
      </li>
      <li>
        <svg viewBox="0 0 24 24" aria-hidden="true"><path d="M7 1h10a2 2 0 0 1 2 2v18a2 2 0 0 1-2 2H7a2 2 0 0 1-2-2V3a2 2 0 0 1 2-2zm0 4v13h10V5zm5 14.5a1 1 0 1 0 0 2 1 1 0 0 0 0-2z"/></svg>
        +44 (0)7700 914362
      </li>
      <li>
        <svg viewBox="0 0 24 24" aria-hidden="true"><path d="M2 5h20v14H2zm2 2v.4l8 5 8-5V7l-8 5z"/></svg>
        mdewhurst@veromb.co.uk
      </li>
      <li>www.veromb.co.uk</li>
    </ul>
  </section>

  <section class="card card-back" aria-label="Business card back">
    <span class="back-square" aria-hidden="true"></span>
    <span class="back-name">VEROMB</span>
  </section>
</main>
</body>
</html>
```